Law Firm Business Card

This is a business card for a law firm that serves US military and veterans.

The card must have ONLY the following (we want an uncluttered look):

- Company logo (PNG, GIF, JPEG copies uploaded)
- A tagline reading: "a law firm for service members and veterans"
- My name and title: "Martin Kovel" and "Attorney"
- My email: "mart.kovel@bramblecourtlegal.com"
- My number: "855-MOKE-TIB (665-3842)"

We are looking for a clean, simple layout with only the above information, likely printed on a bright white cotton stock. The font of our logo is DIN 1451, and the font used on our website is Helvetica Neue. The color of our logo is #336699, and we probably want the tagline in that color also, and my contact information in a dark grey. Please review our website at www.bramblecourtlegal.com to ensure your card design complements our website style.

Thanks and we look forward to seeing your submissions.

A few notes:

- Two-sided submissions are ok
- Please don't add graphics (scales of justice, judges hammer, etc)

```html
<!DOCTYPE html>
<html lang="en">
<head>
<meta charset="utf-8">
<title>Bramble Court Legal – Business Card</title>
<link rel="stylesheet" href="https://fonts.googleapis.com/css2?family=Arimo:wght@400;700&display=swap">
<style>
  :root {
    --brand-blue: #1f6aa5;
    --brand-blue-deep: #13578f;
    --card-white: #ffffff;
    --page-bg: #e6e8eb;
    --text-light: #eef4fa;
  }
  * { box-sizing: border-box; margin: 0; padding: 0; }
  html, body {
    width: 1200px;
    height: 900px;
    overflow: hidden;
    background: var(--page-bg);
    font-family: "Arimo", "Helvetica Neue", Arial, sans-serif;
  }
  .canvas {
    width: 1200px;
    height: 900px;
    display: flex;
    align-items: center;
    justify-content: center;
  }
  .business-card {
    position: relative;
    width: 1000px;
    height: 560px;
    background: var(--card-white);
    box-shadow: 0 10px 30px rgba(0,0,0,0.18);
    overflow: hidden;
  }
  .brand-area {
    height: 190px;
    display: flex;
    align-items: center;
    justify-content: center;
  }
  .brand-name {
    font-family: "Arimo", "Helvetica Neue", Arial, sans-serif;
    font-weight: 700;
    font-size: 64px;
    letter-spacing: 1px;
    color: var(--brand-blue);
    text-transform: uppercase;
  }
  .stripe {
    height: 12px;
    background: var(--brand-blue);
  }
  .tagline-band {
    height: 62px;
    display: flex;
    align-items: center;
    justify-content: center;
  }
  .tagline {
    font-weight: 700;
    font-size: 30px;
    color: var(--brand-blue-deep);
  }
  .stripe-thin {
    height: 8px;
    background: var(--brand-blue);
  }
  .gap-band {
    height: 14px;
  }
  .contact-panel {
    position: absolute;
    left: 0; right: 0; bottom: 0;
    top: 306px;
    background: linear-gradient(180deg, var(--brand-blue) 0%, var(--brand-blue-deep) 100%);
    color: var(--text-light);
    text-align: center;
    padding-top: 22px;
  }
  .person-name {
    font-weight: 700;
    font-size: 34px;
    line-height: 1.1;
  }
  .person-title {
    font-size: 27px;
    line-height: 1.3;
  }
  .divider-stars {
    font-size: 17px;
    letter-spacing: 4px;
    margin-top: 10px;
  }
  .contact-list {
    list-style: none;
    margin-top: 22px;
    display: flex;
    flex-direction: column;
    align-items: center;
    gap: 14px;
    font-size: 28px;
  }
  .contact-item {
    display: flex;
    align-items: center;
    gap: 14px;
  }
  .contact-icon {
    width: 28px;
    height: 28px;
    flex: none;
  }
</style>
</head>
<body>
<main class="canvas">
  <section class="business-card">
    <header class="brand-area">
      <span class="brand-name">Bramble Court Legal</span>
    </header>
    <div class="stripe"></div>
    <div class="tagline-band">
      <p class="tagline">a law firm for service members and veterans</p>
    </div>
    <div class="stripe-thin"></div>
    <div class="gap-band"></div>

    <div class="contact-panel">
      <p class="person-name">Martin Kovel</p>
      <p class="person-title">Attorney</p>
      <p class="divider-stars">★★★★★</p>
      <ul class="contact-list">
        <li class="contact-item">
          <svg class="contact-icon" viewBox="0 0 24 24" aria-hidden="true">
            <text x="12" y="19" text-anchor="middle" font-size="22" font-family="Arimo, Arial, sans-serif" fill="currentColor">@</text>
          </svg>
          <span class="contact-email">mart.kovel@bramblecourtlegal.com</span>
        </li>
        <li class="contact-item">
          <svg class="contact-icon" viewBox="0 0 24 24" aria-hidden="true">
            <path fill="currentColor" d="M6.6 10.8c1.4 2.8 3.8 5.1 6.6 6.6l2.2-2.2c.3-.3.7-.4 1-.2 1.1.4 2.3.6 3.6.6.6 0 1 .4 1 1V20c0 .6-.4 1-1 1C10.6 21 3 13.4 3 4c0-.6.4-1 1-1h3.5c.6 0 1 .4 1 1 0 1.2.2 2.4.6 3.6.1.3 0 .7-.2 1l-2.3 2.2z"/>
          </svg>
          <span class="contact-phone">855-MOKE-TIB (665-3842)</span>
        </li>
      </ul>
    </div>
  </section>
</main>
</body>
</html>
```